Home Page Design

We have a B2B home page design and need a consumer version. The look and feel can look similar but needs to be distinctly different so it in not to get confused. Essentially it should look like the same company with a different model. We will need a PSD w all layers organized and easy to understand. Attached is the logo, B2B comp, and a MS Word doc with a short description. In addition, I have attached a wire frame to be used as a site map. PLEASE DO NOT take that as the creative. I expect to see your creative based on the information provided.

Consumer

```html
<!DOCTYPE html>
<html lang="en">
<head>
<meta charset="utf-8">
<title>GivingSteward.com – Charity Auctions</title>
<link href="https://fonts.googleapis.com/css2?family=Signika:wght@400;600;700&family=Questrial&display=swap" rel="stylesheet">
<style>
:root{
  --blue:#186e9a;
  --heading-blue:#1f6a96;
  --green:#3aa947;
  --dark:#222;
  --text:#333;
  --card:#f4f4f4;
  --footer:#5a5a5a;
  --white:#fff;
}
*{margin:0;padding:0;box-sizing:border-box}
html,body{width:1063px;height:1200px;overflow:hidden;background:var(--white)}
body{position:relative;font-family:Arial,Helvetica,sans-serif;color:var(--text)}
.abs{position:absolute}

.site-header{position:absolute;left:0;top:0;width:1063px;height:86px}
.brand{position:absolute;left:78px;top:20px;display:flex;align-items:center;gap:10px}
.brand-dot{width:36px;height:36px;border-radius:50%;background:var(--blue)}
.brand-name{font-family:"Questrial",sans-serif;font-size:20px;color:var(--green)}
.main-nav{position:absolute;top:31px;left:0;width:1063px;font-family:"Questrial",sans-serif;font-size:11.5px;color:var(--dark)}
.main-nav a{position:absolute;color:inherit;text-decoration:none;white-space:nowrap}
.main-nav a.active::after{content:"";position:absolute;left:-5px;right:-3px;top:17px;height:3px;background:var(--blue)}

.hero{position:absolute;left:0;top:86px;width:1063px;height:391px;
  background:linear-gradient(100deg,#cfc6b8 0%,#a89a86 30%,#5a3f30 50%,#3a2a24 65%,#9a2a25 80%,#c9bfb0 100%)}
.hero-caption{position:absolute;left:158px;top:170px;width:712px;height:98px;background:rgba(60,60,60,.45);text-align:center;color:var(--white)}
.hero-caption h1{font-family:"Signika",sans-serif;font-weight:400;font-size:27px;margin-top:4px}
.hero-caption p{font-size:10.5px;line-height:14px;margin:10px 28px 0}

.search-panel{position:absolute;left:76px;top:530px;width:210px;height:532px;background:var(--blue)}
.ribbon{position:absolute;left:-10px;width:208px;height:26px;background:var(--green);color:var(--white);
  font-family:"Signika",sans-serif;font-weight:600;font-size:23px;line-height:26px;padding-left:24px;
  clip-path:polygon(0 0,92% 0,100% 50%,92% 100%,0 100%)}
.ribbon-fold{position:absolute;left:-10px;width:10px;height:34px;background:var(--dark);border-radius:6px 0 0 6px}
.panel-sub{position:absolute;left:14px;color:var(--white);font-family:"Signika",sans-serif;font-weight:600}
.field{position:absolute;left:13px;width:184px;height:26px;background:var(--white);
  font-family:"Questrial",sans-serif;font-size:12px;color:var(--dark);line-height:26px;padding-left:8px}
.btn{position:absolute;left:113px;width:84px;height:27px;background:var(--green);color:var(--white);
  font-family:"Signika",sans-serif;font-weight:600;font-size:14px;text-align:center;line-height:27px}

.section-title{position:absolute;left:321px;font-family:"Signika",sans-serif;font-weight:600;font-size:20px;color:var(--heading-blue)}
.item-card{position:absolute;top:543px;width:155px;height:213px;background:var(--card)}
.item-photo{position:absolute;left:10px;top:10px;width:134px;height:122px}
.item-title{position:absolute;left:10px;top:143px;width:140px;font-family:"Signika",sans-serif;font-weight:600;font-size:12.5px;line-height:14px;color:var(--heading-blue)}
.item-text{position:absolute;left:10px;top:178px;width:142px;font-size:10.5px;line-height:13px;color:var(--text)}

.event{position:absolute;top:836px;width:150px}
.event-photo{width:149px;height:147px}
.event-title{margin-top:16px;font-family:"Signika",sans-serif;font-weight:600;font-size:10.5px;line-height:13px;color:var(--dark);height:30px}
.event-text{font-size:10px;color:#555;margin-top:2px}
.event-meta{display:flex;align-items:center;gap:4px;font-size:8.5px;color:var(--dark);margin-top:8px;white-space:nowrap}
.event-meta svg{flex:none}

.site-footer{position:absolute;left:0;top:1109px;width:1063px;height:91px;background:var(--footer);color:var(--white)}
.footer-nav{position:absolute;left:87px;top:24px;font-family:"Questrial",sans-serif;font-size:11.5px;white-space:nowrap}
.footer-nav span{margin:0 20px}
.copyright{position:absolute;left:88px;top:50px;font-size:10.5px}
.footer-brand{position:absolute;left:790px;top:26px;display:flex;align-items:center;gap:10px}
.footer-brand .brand-dot{background:var(--white)}
.footer-brand .brand-name{color:var(--white)}
</style>
</head>
<body>

<header class="site-header">
  <div class="brand"><span class="brand-dot"></span><span class="brand-name">GivingSteward.com</span></div>
  <nav class="main-nav">
    <a class="active" href="#" style="left:568px">POST YOUR EVENT</a>
    <a href="#" style="left:704px">ADD AUCTION ITEMS</a>
    <a href="#" style="left:854px">ABOUT</a>
    <a href="#" style="left:929px">CONTACT</a>
  </nav>
</header>

<section class="hero" role="img" aria-label="Photo of smiling schoolchildren in a classroom">
  <div class="hero-caption">
    <h1>Lorem ipsum dolor sit amet</h1>
    <p>Lorem ipsum dolor sit amet, consectetur adipisicing elit, sed do eiusmod tempor incididunt ut labore et dolore magna aliqua. Ut enim ad minim veniam, quis nostrud exercitation ullamco laboris nisi ut aliquip ex ea commodo consequat.</p>
  </div>
</section>

<aside class="search-panel">
  <div class="ribbon-fold" style="top:11px"></div>
  <div class="ribbon" style="top:17px">Search</div>
  <div class="panel-sub" style="top:49px;font-size:13px">FOR AN AUCTION ITEM</div>
  <div class="field" style="top:72px">Auction Type</div>
  <div class="field" style="top:111px">Auction Date</div>
  <div class="field" style="top:151px">Charity</div>
  <div class="btn" style="top:195px">SEARCH</div>

  <div class="ribbon-fold" style="top:256px"></div>
  <div class="ribbon" style="top:262px">Search</div>
  <div class="panel-sub" style="top:289px;left:16px;font-size:15px">for An Auction Item</div>
  <div class="field" style="top:320px;left:11px">Event Type</div>
  <div class="field" style="top:360px;left:11px">Event Date</div>
  <div class="field" style="top:400px;left:11px">Event Location</div>
  <div class="field" style="top:438px;left:11px">Event Name</div>
  <div class="btn" style="top:480px">SEARCH</div>
</aside>

<h2 class="section-title" style="top:505px">FEATURED AUCTION ITEMS</h2>

<article class="item-card" style="left:320px">
  <div class="item-photo" role="img" aria-label="Guests at a formal charity dinner" style="background:linear-gradient(160deg,#4a3a34,#8a6a58 50%,#b02a2a)"></div>
  <h3 class="item-title">DINNER WITH MARCUS REED</h3>
  <p class="item-text">Lorem ipsum dolor sit amet, consectetur adipiscing</p>
</article>
<article class="item-card" style="left:490px">
  <div class="item-photo" role="img" aria-label="Three bottles of wine" style="background:linear-gradient(90deg,#f4f4f4 10%,#3a3f2a 25%,#2a1a20 50%,#c8c48a 75%,#f4f4f4 90%)"></div>
  <h3 class="item-title" style="left:13px">CASE OF VISTA RIDGE WINE</h3>
  <p class="item-text" style="left:14px">Lorem ipsum dolor sit amet, consectetur adipiscing</p>
</article>
<article class="item-card" style="left:661px">
  <div class="item-photo" role="img" aria-label="Road bicycle" style="background:radial-gradient(circle at 50% 55%,#9ab6cc,#f4f4f4 60%)"></div>
  <h3 class="item-title">RIDGELINE BICYCLE</h3>
  <p class="item-text">Lorem ipsum dolor sit amet, consectetur adipiscing</p>
</article>
<article class="item-card" style="left:832px">
  <div class="item-photo" role="img" aria-label="Busy Paris street with classic buildings" style="background:linear-gradient(180deg,#c8c8c4,#a89a88 50%,#4a4440)"></div>
  <h3 class="item-title">5 DAYS/ 4 NIGHTS IN PARIS FRANCE</h3>
  <p class="item-text">Lorem ipsum dolor sit amet, consectetur adipiscing</p>
</article>

<h2 class="section-title" style="top:797px">FEATURED CHARITY EVENTS</h2>

<article class="event" style="left:321px">
  <div class="event-photo" role="img" aria-label="Clubhouse overlooking a golf course" style="background:linear-gradient(180deg,#9cc0e0 0%,#d8d0c0 35%,#7a9a5a 60%,#3a6a2a 100%)"></div>
  <h3 class="event-title">NOVEMBER 12 OAKMERE COUNTRY CLUB</h3>
  <p class="event-text">Lorem ipsum sed do dolore.</p>
  <div class="event-meta"><svg width="12" height="12" viewBox="0 0 12 12"><circle cx="6" cy="6.5" r="4.8" fill="none" stroke="#222" stroke-width="1.2"/><path d="M6 6.5V4M4.5 0.8h3" stroke="#222" stroke-width="1.2"/></svg>03 DEC 2013 <svg width="11" height="11" viewBox="0 0 11 11"><path d="M1 10l1-3 6-6 2 2-6 6z" fill="#222"/></svg>LORE IPSUM</div>
</article>
<article class="event" style="left:494px">
  <div class="event-photo" role="img" aria-label="Desert golf course with mountains" style="background:linear-gradient(180deg,#7aa0c8 0%,#8a6a4a 18%,#4a7a2a 35%,#8ac040 60%,#b89a4a 100%)"></div>
  <h3 class="event-title">NOVEMBER 16 HARBOR DUNES</h3>
  <p class="event-text">Lorem ipsum sed do dolore.</p>
  <div class="event-meta"><svg width="12" height="12" viewBox="0 0 12 12"><circle cx="6" cy="6.5" r="4.8" fill="none" stroke="#222" stroke-width="1.2"/><path d="M6 6.5V4M4.5 0.8h3" stroke="#222" stroke-width="1.2"/></svg>03 DEC 2013 <svg width="11" height="11" viewBox="0 0 11 11"><path d="M1 10l1-3 6-6 2 2-6 6z" fill="#222"/></svg>LORE IPSUM</div>
</article>
<article class="event" style="left:665px">
  <div class="event-photo" role="img" aria-label="Island green surrounded by water" style="background:linear-gradient(180deg,#4a80c8 0%,#2a4a2a 30%,#5aa040 55%,#1a2a4a 75%,#2a60b0 100%)"></div>
  <h3 class="event-title">NOVEMBER 18 LAKESIDE GREENS</h3>
  <p class="event-text">Lorem ipsum sed do dolore.</p>
  <div class="event-meta"><svg width="12" height="12" viewBox="0 0 12 12"><circle cx="6" cy="6.5" r="4.8" fill="none" stroke="#222" stroke-width="1.2"/><path d="M6 6.5V4M4.5 0.8h3" stroke="#222" stroke-width="1.2"/></svg>03 DEC 2013 <svg width="11" height="11" viewBox="0 0 11 11"><path d="M1 10l1-3 6-6 2 2-6 6z" fill="#222"/></svg>LORE IPSUM</div>
</article>
<article class="event" style="left:836px">
  <div class="event-photo" role="img" aria-label="Island green surrounded by water" style="background:linear-gradient(180deg,#4a80c8 0%,#2a4a2a 30%,#5aa040 55%,#1a2a4a 75%,#2a60b0 100%)"></div>
  <h3 class="event-title">NOVEMBER 19 MESA VERDE</h3>
  <p class="event-text">Lorem ipsum sed do dolore.</p>
  <div class="event-meta"><svg width="12" height="12" viewBox="0 0 12 12"><circle cx="6" cy="6.5" r="4.8" fill="none" stroke="#222" stroke-width="1.2"/><path d="M6 6.5V4M4.5 0.8h3" stroke="#222" stroke-width="1.2"/></svg>03 DEC 2013 <svg width="11" height="11" viewBox="0 0 11 11"><path d="M1 10l1-3 6-6 2 2-6 6z" fill="#222"/></svg>LORE IPSUM</div>
</article>

<footer class="site-footer">
  <div class="footer-nav">Post Your event<span>|</span>Add Auction items<span>|</span>About<span>|</span>Contact</div>
  <div class="copyright">Copyright © 2014 All Rights Reserved | Privacy Policy</div>
  <div class="footer-brand"><span class="brand-dot"></span><span class="brand-name">GivingSteward.com</span></div>
</footer>

</body>
</html>
```